Steadfast Carewell (02)

We're designing a website to sell Medicare Supplements. Attached is the content we want to say and general layout, but please use your best knowledge to make it better. This platform is intentionally simplistic because this is reaching an older demographic, so it should be very straightforward, attention-grabbing and extremely user-friendly, while still appearing reliable and professional.
This should be a two-page web design. The homepage has information on Medicare supplements (script in image attached below) along with a button to input zip code. This triggers a window to pop up asking for personal information (will also be listed in attachment).
This brings you to the second page that lists out the medicare supplement companies and plans based on inputed information. We just want to see the design you have in mind, so it doesn't matter what information you put in this section. Feel free to reference/replicate the information in image 3 in the doc. There should be a section where you can filter results by company, premium price, or coverage plans.
Target Market(s)
Seniors, 65+
Industry/Entity Type
Insurance
Number of Pages Required
2 page
Look and feel

```html
<!DOCTYPE html>
<html lang="en">
<head>
<meta charset="utf-8">
<title>Steadfast Carewell – Plans &amp; Quote</title>
<link href="https://fonts.googleapis.com/css2?family=Mulish:wght@400;600;700;800&display=swap" rel="stylesheet">
<style>
:root{
  --red:#e0474c;
  --blue:#2c5e8f;
  --link:#1f5f9e;
  --ink:#222;
  --muted:#444;
  --line:#d9d9d9;
  --soft:#f5f5f5;
  --tint-blue:#eef6fc;
  --tint-red:#fdeeee;
  --white:#fff;
}
*{box-sizing:border-box;margin:0;padding:0}
html,body{width:1200px;height:866px;overflow:hidden;background:var(--white);font-family:"Mulish",sans-serif;color:var(--ink)}
.canvas{position:relative;width:1200px;height:866px}
.page{position:absolute;top:44px;width:1010px;height:1470px;background:var(--white);transform:scale(.5291);transform-origin:0 0;box-shadow:0 0 8px rgba(0,0,0,.12);overflow:hidden}
.page--results{left:48px}
.page--quote{left:618px}

.site-header{position:absolute;left:0;top:0;width:100%;height:104px}
.brand{position:absolute;left:95px;top:18px;display:flex;align-items:center;gap:10px}
.brand-dot{width:56px;height:56px;border-radius:50%;background:var(--blue)}
.brand-name{font-weight:800;font-size:27px;line-height:28px;color:var(--blue)}
.nav{position:absolute;left:523px;top:36px;display:flex;gap:20px;font-size:14px;color:var(--ink)}
.crumbs{position:absolute;left:0;top:104px;width:100%;height:49px;background:var(--red);color:var(--white);font-size:14px;padding:16px 0 0 93px;word-spacing:2px}
.crumbs span{margin:0 10px}

.plan-types{position:absolute;left:0;top:153px;width:100%;height:210px;background:var(--soft)}
.type-box{position:absolute;top:32px;width:267px;height:147px;border:2px solid var(--blue);background:var(--tint-blue);display:flex;align-items:center;justify-content:center;text-align:center;font-size:18px;line-height:26px}
.type-box--active{border-color:var(--red);background:var(--tint-red)}

.section-title{position:absolute;left:0;top:418px;width:100%;text-align:center;color:var(--red);font-weight:700;font-size:25px}

.tool{position:absolute;left:94px;width:199px;height:48px;border:1px solid var(--line);display:flex;align-items:center;color:var(--red);font-size:14px}
.tool-icon{width:50px;height:48px;margin:-1px 8px 0 -1px;background:var(--red);display:flex;align-items:center;justify-content:center}
.filters{position:absolute;left:94px;top:598px;width:199px;height:752px;border:1px solid var(--line);font-size:13px}
.filters-head{height:48px;border-bottom:1px solid var(--line);padding:16px 8px}
.filter-group{border-bottom:1px solid var(--line);padding:18px 8px 14px}
.filter-group:last-child{border-bottom:0}
.filter-title{font-weight:700;display:flex;justify-content:space-between;align-items:center;margin-bottom:10px}
.filter-title::after{content:"";border:6px solid transparent;border-top:7px solid var(--ink);margin-top:7px;margin-right:4px}
.filter-group li{list-style:none;height:26px}

.plan{position:absolute;left:311px;width:605px;height:274px;border:1px solid var(--line);background:var(--white);font-size:15px}
.plan-price{position:absolute;left:0;top:0;width:188px;height:222px;border-right:1px solid var(--line);text-align:center;padding-top:26px}
.amount{font-weight:700;font-size:23px}
.amount-label{font-size:16px;margin-top:4px}
.btn-enroll{display:inline-block;margin-top:12px;width:93px;height:38px;line-height:38px;background:var(--blue);color:var(--white);border-radius:3px;font-size:14px}
.fav{position:absolute;left:25px;top:174px;display:flex;gap:4px;align-items:center;font-size:14px}
.copay{position:absolute;top:0;height:102px;border-bottom:1px solid var(--line);padding-top:26px}
.copay--pcp{left:188px;width:217px;border-right:1px solid var(--line);padding-left:22px}
.copay--spec{left:405px;width:200px;padding-left:36px}
.copay .amount-label{font-size:16px}
.plan-details{position:absolute;left:210px;top:114px;width:390px;font-size:14px}
.plan-details a{color:var(--link);text-decoration:none}
.features{position:relative;margin-top:12px;height:70px}
.feat{position:absolute;white-space:nowrap}
.feat::before{content:"✓";color:var(--red);font-weight:800;margin-right:2px}
.plan-foot{position:absolute;left:0;top:222px;width:100%;height:51px;border-top:1px solid var(--line)}
.more{position:absolute;left:25px;top:17px;color:var(--link);font-size:14px}
.more::after{content:"";display:inline-block;border:5px solid transparent;border-top:7px solid var(--link);margin-left:8px;vertical-align:-3px}
.btn-compare{position:absolute;left:504px;top:4px;width:95px;height:41px;line-height:41px;background:var(--red);color:var(--white);text-align:center;font-weight:700;font-size:16px}

.site-footer{position:absolute;left:94px;top:1398px;width:822px;border-top:1px solid var(--line);text-align:center;padding-top:28px;font-size:13px}

.dim{position:absolute;inset:0;background:rgba(0,0,0,.72)}
.modal{position:absolute;left:167px;top:93px;width:676px;height:580px;background:var(--white);padding:0 39px}
.modal-close{position:absolute;right:12px;top:10px}
.modal h2{margin-top:60px;text-align:center;color:var(--red);font-weight:800;font-size:28px}
.modal-intro{margin:12px -18px 0;text-align:center;font-size:12px;line-height:20px;color:var(--muted)}
.field-label{position:absolute;font-weight:700;font-size:16px}
.field-label b{color:var(--red);font-weight:700}
.check{position:absolute;left:39px;display:flex;align-items:center;gap:8px;font-size:13px;color:var(--muted)}
.check i{width:13px;height:13px;border:1px solid #bbb;display:block}
.input{position:absolute;width:233px;height:40px;border:1px solid var(--line);font-size:12px;color:var(--muted);padding:12px 10px}
.select::after{content:"";position:absolute;right:10px;top:16px;border:5px solid transparent;border-top:7px solid var(--ink)}
.btn-submit{position:absolute;left:291px;top:498px;width:104px;height:40px;line-height:40px;background:var(--red);color:var(--white);text-align:center;font-weight:700;font-size:16px}
</style>
</head>
<body>
<div class="canvas">

<!-- Results page -->
<section class="page page--results">
  <header class="site-header">
    <div class="brand"><span class="brand-dot"></span><span class="brand-name">Steadfast<br>Carewell</span></div>
    <nav class="nav"><span>Find Medicare Plans</span><span>Learn About Medicare</span><span>Favourites</span></nav>
  </header>
  <div class="crumbs">Female<span>/</span>54yrs<span>/</span>Add Doctors<span>/</span>Add Drugs</div>
  <div class="plan-types">
    <div class="type-box" style="left:94px">Medicare Advantage Plans<br>3 plans available</div>
    <div class="type-box type-box--active" style="left:372px">Medicare Supplement<br>Insurance Plans<br>21 plans available</div>
    <div class="type-box" style="left:650px">Medicare Part D Plans 23<br>plans available</div>
  </div>
  <h1 class="section-title">Steadfast Carewell Advantage Plans</h1>

  <div class="tool" style="top:483px"><span class="tool-icon"><svg width="26" height="26" viewBox="0 0 26 26" fill="none" stroke="#fff" stroke-width="1.8"><circle cx="13" cy="8" r="5"/><path d="M3 24c0-6 4-9 10-9s10 3 10 9z"/></svg></span>Add Your Doctors</div>
  <div class="tool" style="top:540px"><span class="tool-icon"><svg width="26" height="26" viewBox="0 0 26 26" fill="none" stroke="#fff" stroke-width="1.8"><rect x="3" y="7" width="20" height="16"/><rect x="5" y="3" width="16" height="4"/><path d="M13 11v8M9 15h8"/></svg></span>Add Your Drugs</div>
  <aside class="filters">
    <div class="filters-head">Filter Plans By:</div>
    <div class="filter-group"><div class="filter-title">Company</div><ul><li>Nemo enim ipsam</li><li>Voluptatem quia voluptas</li><li>Sit aspernatur aut odit</li><li>Aut fugit sed quia</li></ul></div>
    <div class="filter-group"><div class="filter-title">Monthly Premium</div><ul><li>Nemo enim ipsam</li><li>Voluptatem quia voluptas</li><li>Sit aspernatur aut odit</li><li>Aut fugit sed quia</li></ul></div>
    <div class="filter-group"><div class="filter-title">Plan Features</div><ul><li>Nemo enim ipsam</li><li>Voluptatem quia voluptas</li><li>Sit aspernatur aut odit</li><li>Aut fugit sed quia</li></ul></div>
    <div class="filter-group"><div class="filter-title">Plan Type</div><ul><li>Nemo enim ipsam</li><li>Voluptatem quia voluptas</li><li>Sit aspernatur aut odit</li><li>Aut fugit sed quia</li><li>Voluptatem quia voluptas</li><li>Sit aspernatur aut odit</li></ul></div>
  </aside>

  <article class="plan" style="top:483px">
    <div class="plan-price"><div class="amount">$60.00</div><div class="amount-label">Monthly Premium</div><span class="btn-enroll">Enroll Now</span>
      <div class="fav"><svg width="18" height="16" viewBox="0 0 18 16"><path d="M9 15S1 10 1 5a4 4 0 0 1 8-1 4 4 0 0 1 8 1c0 5-8 10-8 10z" fill="none" stroke="#e0474c" stroke-width="1.6"/></svg>Add To Favourites</div></div>
    <div class="copay copay--pcp"><div class="amount">$5</div><div class="amount-label">Primary Doctor Co-pay</div></div>
    <div class="copay copay--spec"><div class="amount">$5</div><div class="amount-label">Specialist Co-pay</div></div>
    <div class="plan-details">Doctors Coverage: <a>Add your doctors to see coverage</a>
      <div class="features"><span class="feat" style="left:0;top:0;margin-left:-12px">​</span><span style="position:absolute;left:0;top:0">Plan Features:</span><span class="feat" style="left:112px;top:0">RX Drugs</span><span class="feat" style="left:112px;top:22px">Hearing</span><span class="feat" style="left:112px;top:43px">Chiropractic Care</span><span class="feat" style="left:286px;top:0">Dental</span><span class="feat" style="left:286px;top:22px">Vision</span></div></div>
    <div class="plan-foot"><span class="more">View More Details</span><span class="btn-compare">Compare</span></div>
  </article>
  <article class="plan" style="top:779px">
    <div class="plan-price"><div class="amount">$60.00</div><div class="amount-label">Monthly Premium</div><span class="btn-enroll">Enroll Now</span>
      <div class="fav"><svg width="18" height="16" viewBox="0 0 18 16"><path d="M9 15S1 10 1 5a4 4 0 0 1 8-1 4 4 0 0 1 8 1c0 5-8 10-8 10z" fill="none" stroke="#e0474c" stroke-width="1.6"/></svg>Add To Favourites</div></div>
    <div class="copay copay--pcp"><div class="amount">$5</div><div class="amount-label">Primary Doctor Co-pay</div></div>
    <div class="copay copay--spec"><div class="amount">$5</div><div class="amount-label">Specialist Co-pay</div></div>
    <div class="plan-details">Doctors Coverage: <a>Add your doctors to see coverage</a>
      <div class="features"><span style="position:absolute;left:0;top:0">Plan Features:</span><span class="feat" style="left:112px;top:0">RX Drugs</span><span class="feat" style="left:112px;top:22px">Hearing</span><span class="feat" style="left:112px;top:43px">Chiropractic Care</span><span class="feat" style="left:286px;top:0">Dental</span><span class="feat" style="left:286px;top:22px">Vision</span></div></div>
    <div class="plan-foot"><span class="more">View More Details</span><span class="btn-compare">Compare</span></div>
  </article>
  <article class="plan" style="top:1075px">
    <div class="plan-price"><div class="amount">$60.00</div><div class="amount-label">Monthly Premium</div><span class="btn-enroll">Enroll Now</span>
      <div class="fav"><svg width="18" height="16" viewBox="0 0 18 16"><path d="M9 15S1 10 1 5a4 4 0 0 1 8-1 4 4 0 0 1 8 1c0 5-8 10-8 10z" fill="none" stroke="#e0474c" stroke-width="1.6"/></svg>Add To Favourites</div></div>
    <div class="copay copay--pcp"><div class="amount">$5</div><div class="amount-label">Primary Doctor Co-pay</div></div>
    <div class="copay copay--spec"><div class="amount">$5</div><div class="amount-label">Specialist Co-pay</div></div>
    <div class="plan-details">Doctors Coverage: <a>Add your doctors to see coverage</a>
      <div class="features"><span style="position:absolute;left:0;top:0">Plan Features:</span><span class="feat" style="left:112px;top:0">RX Drugs</span><span class="feat" style="left:112px;top:22px">Hearing</span><span class="feat" style="left:112px;top:43px">Chiropractic Care</span><span class="feat" style="left:286px;top:0">Dental</span><span class="feat" style="left:286px;top:22px">Vision</span></div></div>
    <div class="plan-foot"><span class="more">View More Details</span><span class="btn-compare">Compare</span></div>
  </article>

  <footer class="site-footer">Copyrights @ 2020 Steadfast Carewell. All Rights Reserved.</footer>
</section>

<!-- Quote modal over results page -->
<section class="page page--quote">
  <header class="site-header">
    <div class="brand"><span class="brand-dot"></span><span class="brand-name">Steadfast<br>Carewell</span></div>
    <nav class="nav"><span>Find Medicare Plans</span><span>Learn About Medicare</span><span>Favourites</span></nav>
  </header>
  <div class="crumbs">Female<span>/</span>54yrs<span>/</span>Add Doctors<span>/</span>Add Drugs</div>
  <div class="plan-types">
    <div class="type-box" style="left:94px">Medicare Advantage Plans<br>3 plans available</div>
    <div class="type-box type-box--active" style="left:372px">Medicare Supplement<br>Insurance Plans<br>21 plans available</div>
    <div class="type-box" style="left:650px">Medicare Part D Plans 23<br>plans available</div>
  </div>
  <h1 class="section-title">Steadfast Carewell Advantage Plans</h1>

  <div class="tool" style="top:483px"><span class="tool-icon"><svg width="26" height="26" viewBox="0 0 26 26" fill="none" stroke="#fff" stroke-width="1.8"><circle cx="13" cy="8" r="5"/><path d="M3 24c0-6 4-9 10-9s10 3 10 9z"/></svg></span>Add Your Doctors</div>
  <div class="tool" style="top:540px"><span class="tool-icon"><svg width="26" height="26" viewBox="0 0 26 26" fill="none" stroke="#fff" stroke-width="1.8"><rect x="3" y="7" width="20" height="16"/><rect x="5" y="3" width="16" height="4"/><path d="M13 11v8M9 15h8"/></svg></span>Add Your Drugs</div>
  <aside class="filters">
    <div class="filters-head">Filter Plans By:</div>
    <div class="filter-group"><div class="filter-title">Company</div><ul><li>Nemo enim ipsam</li><li>Voluptatem quia voluptas</li><li>Sit aspernatur aut odit</li><li>Aut fugit sed quia</li></ul></div>
    <div class="filter-group"><div class="filter-title">Monthly Premium</div><ul><li>Nemo enim ipsam</li><li>Voluptatem quia voluptas</li><li>Sit aspernatur aut odit</li><li>Aut fugit sed quia</li></ul></div>
    <div class="filter-group"><div class="filter-title">Plan Features</div><ul><li>Nemo enim ipsam</li><li>Voluptatem quia voluptas</li><li>Sit aspernatur aut odit</li><li>Aut fugit sed quia</li></ul></div>
    <div class="filter-group"><div class="filter-title">Plan Type</div><ul><li>Nemo enim ipsam</li><li>Voluptatem quia voluptas</li><li>Sit aspernatur aut odit</li><li>Aut fugit sed quia</li><li>Voluptatem quia voluptas</li><li>Sit aspernatur aut odit</li></ul></div>
  </aside>

  <article class="plan" style="top:483px">
    <div class="plan-price"><div class="amount">$60.00</div><div class="amount-label">Monthly Premium</div><span class="btn-enroll">Enroll Now</span>
      <div class="fav"><svg width="18" height="16" viewBox="0 0 18 16"><path d="M9 15S1 10 1 5a4 4 0 0 1 8-1 4 4 0 0 1 8 1c0 5-8 10-8 10z" fill="none" stroke="#e0474c" stroke-width="1.6"/></svg>Add To Favourites</div></div>
    <div class="copay copay--pcp"><div class="amount">$5</div><div class="amount-label">Primary Doctor Co-pay</div></div>
    <div class="copay copay--spec"><div class="amount">$5</div><div class="amount-label">Specialist Co-pay</div></div>
    <div class="plan-details">Doctors Coverage: <a>Add your doctors to see coverage</a>
      <div class="features"><span style="position:absolute;left:0;top:0">Plan Features:</span><span class="feat" style="left:112px;top:0">RX Drugs</span><span class="feat" style="left:112px;top:22px">Hearing</span><span class="feat" style="left:112px;top:43px">Chiropractic Care</span><span class="feat" style="left:286px;top:0">Dental</span><span class="feat" style="left:286px;top:22px">Vision</span></div></div>
    <div class="plan-foot"><span class="more">View More Details</span><span class="btn-compare">Compare</span></div>
  </article>
  <article class="plan" style="top:779px">
    <div class="plan-price"><div class="amount">$60.00</div><div class="amount-label">Monthly Premium</div><span class="btn-enroll">Enroll Now</span>
      <div class="fav"><svg width="18" height="16" viewBox="0 0 18 16"><path d="M9 15S1 10 1 5a4 4 0 0 1 8-1 4 4 0 0 1 8 1c0 5-8 10-8 10z" fill="none" stroke="#e0474c" stroke-width="1.6"/></svg>Add To Favourites</div></div>
    <div class="copay copay--pcp"><div class="amount">$5</div><div class="amount-label">Primary Doctor Co-pay</div></div>
    <div class="copay copay--spec"><div class="amount">$5</div><div class="amount-label">Specialist Co-pay</div></div>
    <div class="plan-details">Doctors Coverage: <a>Add your doctors to see coverage</a>
      <div class="features"><span style="position:absolute;left:0;top:0">Plan Features:</span><span class="feat" style="left:112px;top:0">RX Drugs</span><span class="feat" style="left:112px;top:22px">Hearing</span><span class="feat" style="left:112px;top:43px">Chiropractic Care</span><span class="feat" style="left:286px;top:0">Dental</span><span class="feat" style="left:286px;top:22px">Vision</span></div></div>
    <div class="plan-foot"><span class="more">View More Details</span><span class="btn-compare">Compare</span></div>
  </article>
  <article class="plan" style="top:1075px">
    <div class="plan-price"><div class="amount">$60.00</div><div class="amount-label">Monthly Premium</div><span class="btn-enroll">Enroll Now</span>
      <div class="fav"><svg width="18" height="16" viewBox="0 0 18 16"><path d="M9 15S1 10 1 5a4 4 0 0 1 8-1 4 4 0 0 1 8 1c0 5-8 10-8 10z" fill="none" stroke="#e0474c" stroke-width="1.6"/></svg>Add To Favourites</div></div>
    <div class="copay copay--pcp"><div class="amount">$5</div><div class="amount-label">Primary Doctor Co-pay</div></div>
    <div class="copay copay--spec"><div class="amount">$5</div><div class="amount-label">Specialist Co-pay</div></div>
    <div class="plan-details">Doctors Coverage: <a>Add your doctors to see coverage</a>
      <div class="features"><span style="position:absolute;left:0;top:0">Plan Features:</span><span class="feat" style="left:112px;top:0">RX Drugs</span><span class="feat" style="left:112px;top:22px">Hearing</span><span class="feat" style="left:112px;top:43px">Chiropractic Care</span><span class="feat" style="left:286px;top:0">Dental</span><span class="feat" style="left:286px;top:22px">Vision</span></div></div>
    <div class="plan-foot"><span class="more">View More Details</span><span class="btn-compare">Compare</span></div>
  </article>

  <footer class="site-footer">Copyrights @ 2020 Steadfast Carewell. All Rights Reserved.</footer>

  <div class="dim"></div>
  <div class="modal" role="dialog" aria-label="Get a quote">
    <svg class="modal-close" width="20" height="20" viewBox="0 0 20 20" stroke="#222" stroke-width="2.4"><path d="M3 3l14 14M17 3L3 17"/></svg>
    <h2>GET A QUOTE</h2>
    <p class="modal-intro">Nemo enim ipsam voluptatem quia voluptas sit aspernatur aut odit aut fugit, sed quia consequuntur magni dolores eos qui ratione voluptatem sequi nesciunt.</p>

    <span class="field-label" style="left:39px;top:200px">Gender<b>*</b></span>
    <span class="check" style="top:236px"><i></i>Male</span>
    <span class="check" style="top:258px"><i></i>Female</span>

    <span class="field-label" style="left:39px;top:294px">Age<b>*</b></span>
    <span class="field-label" style="left:291px;top:294px">Date of Birth<b>*</b></span>
    <div class="input" style="left:39px;top:325px"></div>
    <div class="input" style="left:291px;top:325px">MM/DD/YY</div>

    <span class="field-label" style="left:39px;top:381px">Hospital Insurance (Part A)</span>
    <span class="field-label" style="left:291px;top:381px">Medical Insurance (Part B)</span>
    <div class="input select" style="left:39px;top:412px">Part A Month</div>
    <div class="input select" style="left:291px;top:412px">Part B Month</div>

    <span class="field-label" style="left:39px;top:468px">Desired Coverage Start Date</span>
    <div class="input" style="left:39px;top:498px"></div>
    <span class="btn-submit">Submit</span>
  </div>
</section>

</div>
</body>
</html>
```